The Pebble Lantern Business Card

I need a business card designed for The Pebble Lantern. The company provides on site support and education to end consumers in the ins and outs of all our digital devices. We advise on product purchase, installation, maintenance and troubleshooting. Anything from cordless phones to home networks.
My initial concept is double sided with the white logo on green on one side and contact details and a small logo on the flip side (logo package attached)
Contact Details:
Marty Fenwick
Managing Director
PO Box 3
Kingsford, NSW 2047
Phone: 0438 605 193
email: marty@pebblelantern.com.au
web: www.pebblelantern.com.au
Target Market(s)
Busy professionals and retired folks.
Industry/Entity Type
Education
Look and feel

```html
<!DOCTYPE html>
<html lang="en">
<head>
<meta charset="utf-8">
<title>The Pebble Lantern – Business Card</title>
<link href="https://fonts.googleapis.com/css2?family=Exo+2:wght@300;400&family=Oswald:wght@500&display=swap" rel="stylesheet">
<style>
  :root {
    --page-bg: #e8e5de;
    --card-white: #ffffff;
    --leaf-green: #7ab33a;
    --deep-navy: #0e2b3f;
    --text-white: #ffffff;
    --logo-navy: #1c3246;
  }
  * { box-sizing: border-box; margin: 0; padding: 0; }
  html, body {
    width: 1200px;
    height: 1018px;
    overflow: hidden;
    background: var(--page-bg);
  }
  .card-sheet {
    position: relative;
    width: 1200px;
    height: 1018px;
    display: flex;
    flex-direction: column;
    align-items: center;
    justify-content: center;
    gap: 46px;
  }
  .business-card {
    position: relative;
    width: 760px;
    height: 434px;
    flex: none;
    background: var(--card-white);
    box-shadow: 0 8px 26px rgba(0, 0, 0, 0.18);
    font-family: "Exo 2", sans-serif;
    overflow: hidden;
  }

  /* Front */
  .card-front {
    display: flex;
    flex-direction: column;
  }
  .brand-panel {
    height: 245px;
    display: flex;
    align-items: center;
    padding-left: 128px;
  }
  .brand-logo {
    display: flex;
    align-items: center;
    gap: 18px;
  }
  .brand-mark {
    width: 48px;
    height: 48px;
    border-radius: 50%;
    background: var(--leaf-green);
  }
  .brand-name {
    font-weight: 300;
    font-size: 39px;
    letter-spacing: 1px;
    color: var(--logo-navy);
    white-space: nowrap;
  }
  .contact-band {
    height: 90px;
    background: var(--leaf-green);
    display: flex;
    align-items: center;
    padding-left: 50px;
    gap: 50px;
    color: var(--text-white);
    font-size: 16px;
    font-weight: 400;
  }
  .contact-column {
    display: flex;
    flex-direction: column;
    gap: 10px;
  }
  .contact-line {
    display: flex;
    align-items: center;
    gap: 10px;
    white-space: nowrap;
  }
  .contact-icon {
    width: 17px;
    height: 17px;
    flex: none;
  }
  .identity-band {
    flex: 1;
    background: var(--deep-navy);
    display: flex;
    justify-content: space-between;
    align-items: center;
    padding: 0 50px;
    color: var(--text-white);
  }
  .person-name {
    font-family: "Oswald", sans-serif;
    font-weight: 500;
    font-size: 30px;
    letter-spacing: 1px;
    text-transform: uppercase;
    line-height: 1.1;
  }
  .person-role {
    font-weight: 400;
    font-size: 14px;
    letter-spacing: 1.5px;
    text-transform: uppercase;
  }
  .postal-address {
    font-style: normal;
    font-weight: 300;
    font-size: 20px;
    line-height: 1.35;
    letter-spacing: 0.5px;
  }

  /* Back */
  .back-stripe {
    position: absolute;
    top: 0;
    bottom: 0;
    background: var(--deep-navy);
  }
  .back-stripe-wide {
    left: 250px;
    width: 150px;
  }
  .back-stripe-edge {
    right: 0;
    width: 70px;
  }
</style>
</head>
<body>
  <main class="card-sheet">
    <section class="business-card card-front" aria-label="Card front">
      <div class="brand-panel">
        <div class="brand-logo">
          <span class="brand-mark"></span>
          <span class="brand-name">The Pebble Lantern</span>
        </div>
      </div>

      <div class="contact-band">
        <div class="contact-column">
          <div class="contact-line">
            <svg class="contact-icon" viewBox="0 0 24 24" aria-hidden="true">
              <path fill="#fff" d="M6.6 10.8a15.1 15.1 0 0 0 6.6 6.6l2.2-2.2a1 1 0 0 1 1-.25 11.4 11.4 0 0 0 3.6.57 1 1 0 0 1 1 1V20a1 1 0 0 1-1 1A17 17 0 0 1 3 4a1 1 0 0 1 1-1h3.5a1 1 0 0 1 1 1c0 1.25.2 2.45.57 3.57a1 1 0 0 1-.25 1z"/>
            </svg>
            <span>0438 605 193</span>
          </div>
          <div class="contact-line">
            <svg class="contact-icon" viewBox="0 0 24 24" aria-hidden="true">
              <rect x="6" y="2" width="12" height="20" rx="2" fill="none" stroke="#fff" stroke-width="2"/>
              <circle cx="12" cy="18" r="1.2" fill="#fff"/>
            </svg>
            <span>0438 605 193</span>
          </div>
        </div>
        <div class="contact-column">
          <div class="contact-line">
            <svg class="contact-icon" viewBox="0 0 24 24" aria-hidden="true">
              <rect x="2" y="5" width="20" height="14" rx="1.5" fill="none" stroke="#fff" stroke-width="2"/>
              <path d="M2.5 6l9.5 7 9.5-7" fill="none" stroke="#fff" stroke-width="2"/>
            </svg>
            <span>marty@pebblelantern.com.au</span>
          </div>
          <div class="contact-line">
            <svg class="contact-icon" viewBox="0 0 24 24" aria-hidden="true">
              <circle cx="12" cy="12" r="9.5" fill="none" stroke="#fff" stroke-width="2"/>
              <ellipse cx="12" cy="12" rx="4" ry="9.5" fill="none" stroke="#fff" stroke-width="1.6"/>
              <path d="M2.5 12h19M4 7h16M4 17h16" stroke="#fff" stroke-width="1.4"/>
            </svg>
            <span>www.pebblelantern.com.au</span>
          </div>
        </div>
      </div>

      <div class="identity-band">
        <div class="person">
          <p class="person-name">Marty Fenwick</p>
          <p class="person-role">Managing Director</p>
        </div>
        <address class="postal-address">
          PO Box 3<br>
          Kingsford, NSW 2047
        </address>
      </div>
    </section>

    <section class="business-card card-back" aria-label="Card back">
      <span class="back-stripe back-stripe-wide"></span>
      <span class="back-stripe back-stripe-edge"></span>
    </section>
  </main>
</body>
</html>
```